Luxury Business Card Design for High-End Window Treatments

Gilded Vantages
Custom Plantation Shutters & Architectural Shading Systems

⸻

BACK

Daniel Forsythe
Owner

Custom Interior & Exterior Window Treatments

919-482-7034
gildedvantages.com

I have included a picture that I’m hoping we can use on the back, but I’m also wondering if you can get rid of the ladder? Should we get rid of shutters , shades and blinds underneath Gilded Vantages?

Target Market(s)

High-end residential homeowners, custom home builders, architects, interior designers, and luxury renovation clients seeking premium plantation shutters and motorized architectural shading systems.

Industry/Entity Type

Custom Window treatments

Contact Information for Business Card

Front Gilded Vantages Custom Plantation Shutters Motorized Architectural Shading Systems BACK Daniel Forsythe Owner 919-482-7034 GildedVantages.com Custom Interior & Exterior Window Treatments By Appointment

Requirements
Nice to have
• Not 100% sure on nice to halves or the color but you can definitely check out my website to get a better understanding of what I’m trying to do

```html
<!DOCTYPE html>
<html lang="en">
<head>
<meta charset="utf-8">
<title>Gilded Vantages – Business Card</title>
<link href="https://fonts.googleapis.com/css2?family=Poppins:wght@400;500;800&display=swap" rel="stylesheet">
<style>
  :root {
    --canvas: #e4e4e4;
    --gold: #c9a84a;
    --gold-deep: #b89a45;
    --photo-light: #c7b57a;
    --photo-mid: #a2925e;
    --photo-dark: #6f6440;
    --ink: #0d0d0d;
    --black: #060708;
    --foil: #c8a845;
  }
  * { box-sizing: border-box; margin: 0; padding: 0; }
  html, body { width: 1200px; height: 1200px; overflow: hidden; }
  body {
    background: var(--canvas);
    font-family: "Poppins", sans-serif;
    position: relative;
  }
  .card {
    position: absolute;
    left: 155px;
    width: 890px;
    height: 506px;
    overflow: hidden;
  }
  /* Front side */
  .card-front { top: 69px; background: var(--gold); color: var(--ink); }
  .scene-photo {
    position: absolute;
    top: 0; right: 0; bottom: 0;
    width: 66%;
    background:
      linear-gradient(90deg, var(--gold) 0%, rgba(201,168,74,0.55) 22%, rgba(201,168,74,0) 55%),
      linear-gradient(180deg, var(--photo-light) 0%, var(--photo-mid) 55%, var(--photo-dark) 100%);
  }
  .headline {
    position: absolute;
    left: 62px; top: 70px;
    font-weight: 800;
    font-size: 37px;
    line-height: 1.4;
    text-transform: uppercase;
    letter-spacing: -0.2px;
  }
  .person-name {
    position: absolute;
    left: 62px; top: 242px;
    font-weight: 500;
    font-size: 36px;
    line-height: 1.2;
  }
  .person-title {
    position: absolute;
    left: 62px; top: 289px;
    font-size: 20px;
    font-weight: 400;
  }
  .contact-list {
    position: absolute;
    left: 62px; top: 368px;
    list-style: none;
    font-size: 22px;
    font-weight: 400;
  }
  .contact-item {
    display: flex;
    align-items: center;
    gap: 14px;
    height: 43px;
  }
  .contact-icon { width: 20px; height: 20px; flex: none; }

  /* Back side */
  .card-back { top: 631px; background: var(--black); }
  .brand {
    position: absolute;
    left: 0; right: 0; top: 115px;
    text-align: center;
    color: var(--foil);
  }
  .brand-name {
    font-weight: 400;
    font-size: 60px;
    line-height: 1.2;
  }
  .brand-services {
    margin-top: 18px;
    font-weight: 400;
    font-size: 30px;
    word-spacing: 14px;
  }
</style>
</head>
<body>

<section class="card card-front">
  <div class="scene-photo" role="img" aria-label="Photo of a covered porch on a stone-chimney home with Adirondack chairs, tinted gold"></div>
  <h1 class="headline">Custom Interior &amp; Exterior<br>Window Treatments</h1>
  <p class="person-name">Daniel Forsythe</p>
  <p class="person-title">Owner</p>
  <ul class="contact-list">
    <li class="contact-item">
      <svg class="contact-icon" viewBox="0 0 24 24" fill="none" stroke="currentColor" stroke-width="2" stroke-linecap="round" stroke-linejoin="round">
        <path d="M22 16.9v3a2 2 0 0 1-2.2 2 19.8 19.8 0 0 1-8.6-3.1 19.5 19.5 0 0 1-6-6A19.8 19.8 0 0 1 2.1 4.2 2 2 0 0 1 4.1 2h3a2 2 0 0 1 2 1.7c.1.9.4 1.8.7 2.7a2 2 0 0 1-.5 2.1L8 9.8a16 16 0 0 0 6 6l1.3-1.3a2 2 0 0 1 2.1-.4c.9.3 1.8.6 2.7.7a2 2 0 0 1 1.7 2z"/>
      </svg>
      <span>919-482-7034</span>
    </li>
    <li class="contact-item">
      <svg class="contact-icon" viewBox="0 0 24 24" fill="none" stroke="currentColor" stroke-width="2">
        <circle cx="12" cy="12" r="10"/>
        <path d="M2 12h20M12 2a15 15 0 0 1 0 20M12 2a15 15 0 0 0 0 20"/>
      </svg>
      <span>gildedvantages.com</span>
    </li>
  </ul>
</section>

<section class="card card-back">
  <div class="brand">
    <p class="brand-name">Gilded<br>Vantages</p>
    <p class="brand-services">Shutters Shades Blinds</p>
  </div>
</section>

</body>
</html>
```